Design a New Business Card for Our Company

We are looking for fresh, unique, and a modern business card that reflects our roots as digital marketing agency focused on SEM.

Industry/Entity Type

Marketing

Contact Information for Business Card

looking for very unique out of the box designs. clean and modern that compliments our logo

Requirements
Must have
• colors should match our logo
• Front should have name, address, email, and phone/fax of the person, phone/fax are the same number
• back should have our url

```html
<!DOCTYPE html>
<html lang="en">
<head>
<meta charset="utf-8">
<title>Brightpath Media – Business Card</title>
<link rel="stylesheet" href="https://fonts.googleapis.com/css2?family=Montserrat:wght@400;500;600;700&display=swap">
<style>
  :root {
    --canvas: #2b2b2d;
    --card: #050506;
    --blue: #5b9bd9;
    --white: #e9e9ea;
    --grey: #b9b9bb;
  }
  html, body {
    margin: 0;
    padding: 0;
    width: 1200px;
    height: 900px;
    overflow: hidden;
    background: var(--canvas);
    font-family: "Montserrat", sans-serif;
  }
  .stage {
    position: relative;
    width: 1200px;
    height: 900px;
  }
  .card {
    position: absolute;
    width: 560px;
    height: 320px;
    background: var(--card);
    border-radius: 22px;
    overflow: hidden;
    box-shadow: 0 18px 40px rgba(0,0,0,.45);
  }
  /* back side */
  .card--back { left: 90px; top: 90px; }
  .card--back .brand {
    position: absolute;
    left: 0; right: 0; top: 118px;
    display: flex;
    justify-content: center;
    align-items: center;
    gap: 14px;
    color: var(--white);
    font-weight: 700;
    font-size: 40px;
    letter-spacing: -0.5px;
  }
  .brand__dot {
    width: 22px; height: 22px;
    border-radius: 50%;
    background: var(--blue);
    flex: none;
  }
  .card--back .url {
    position: absolute;
    left: 0; right: 0; bottom: 34px;
    text-align: center;
    color: var(--white);
    font-size: 15px;
  }
  .url b { color: var(--blue); font-weight: 500; }

  /* front side */
  .card--front { left: 550px; top: 490px; }
  .card--front .brand {
    position: absolute;
    left: 36px; top: 40px;
    display: flex;
    align-items: center;
    gap: 12px;
    color: var(--white);
    font-weight: 700;
    font-size: 34px;
    letter-spacing: -0.5px;
  }
  .card--front .brand__dot { width: 18px; height: 18px; }
  .accent-bar {
    position: absolute;
    left: 0; top: 138px;
    width: 28px; height: 34px;
    background: var(--blue);
  }
  .person {
    position: absolute;
    left: 42px; top: 128px;
  }
  .person__name {
    margin: 0;
    color: var(--blue);
    font-weight: 600;
    font-size: 22px;
    letter-spacing: .5px;
  }
  .person__role {
    margin: 0;
    color: var(--grey);
    font-size: 14px;
  }
  .address {
    position: absolute;
    left: 72px; top: 188px;
    margin: 0;
    color: var(--white);
    font-size: 14px;
    line-height: 19px;
    font-style: normal;
  }
  .contacts {
    position: absolute;
    left: 72px; top: 236px;
    margin: 0; padding: 0;
    list-style: none;
    color: var(--white);
    font-size: 13.5px;
    line-height: 17px;
  }
  .contacts li { display: flex; align-items: center; gap: 9px; }
  .contacts svg { width: 11px; height: 11px; fill: var(--blue); flex: none; }
</style>
</head>
<body>
<main class="stage">

  <section class="card card--back" aria-label="Card back">
    <div class="brand"><span class="brand__dot"></span>Brightpath Media</div>
    <p class="url">www.<b>brightpathmedia</b>.com</p>
  </section>

  <section class="card card--front" aria-label="Card front">
    <div class="brand"><span class="brand__dot"></span>Brightpath Media</div>

    <span class="accent-bar"></span>
    <div class="person">
      <p class="person__name">Marcus Ellery</p>
      <p class="person__role">Director</p>
    </div>

    <address class="address">PO Box 517 Hillcrest<br>NSW Australia 2108</address>

    <ul class="contacts">
      <li>
        <svg viewBox="0 0 12 12"><path d="M2.5 1h2l1 2.5-1.3 1a6 6 0 0 0 3.3 3.3l1-1.3L11 7.5v2a1 1 0 0 1-1 1A9 9 0 0 1 1.5 2a1 1 0 0 1 1-1z"/></svg>
        +330 5812-4490
      </li>
      <li>
        <svg viewBox="0 0 12 12"><rect x="3" y="1" width="6" height="3"/><rect x="1" y="4.5" width="10" height="5" rx="1"/><rect x="3" y="8" width="6" height="3"/></svg>
        +330 5812-4491
      </li>
      <li>
        <svg viewBox="0 0 12 12"><path d="M1 2.5h10v7H1z M1.8 3.2 6 6.3l4.2-3.1" fill="none" stroke="#5b9bd9" stroke-width="1.2"/></svg>
        info@brightpathmedia.com
      </li>
      <li>
        <svg viewBox="0 0 12 12"><circle cx="6" cy="6" r="5" fill="none" stroke="#5b9bd9" stroke-width="1.1"/><path d="M1 6h10M6 1c-2.5 2.8-2.5 7.2 0 10M6 1c2.5 2.8 2.5 7.2 0 10" fill="none" stroke="#5b9bd9" stroke-width="1"/></svg>
        <span class="url">www.<b>brightpathmedia</b>.com</span>
      </li>
    </ul>
  </section>

</main>
</body>
</html>
```